Community grantmaker building brochure site

The Selvane Community Trust is a grant-making agency that seeks to build an emotionally engaging and informative site that portrays Haiti from an asset lens. We want to focus on the opportunities for growth while highlighting the current opportunity to give to a worthy cause.

Users will be Haitians, Friends of Haiti, and Media who are potential donors, innovators and decision makers.

We envision a home page with a horizontal navigation bar (with About us, Impact/Our work/Projects, Donate, Contact us, Meet the team, and Haiti’s assets/facts/resources/research) a series of large horizontal images (with dissolving motion) and language underneath the image that describes who we are and what we do.

We currently have content for the tabs below:

About us: Selvane Community Trust - The Trust is the country’s first endowed fund building on Haiti’s assets while providing resources for scalable solutions.

The Trust addresses three essential pillars for a thriving Ayiti: environment, entrepreneurship, and civic education. We will invest in water resources focusing in an integrative and systemic way on the lasting impact of this approach.

Donate: A link to the Corvell Foundation and statement about Hurricane Bertrand. “Giving for Outcomes”

Sustainable Funding: Links to articles and resources that show our theory of change while highlighting facts about Haiti.

Meet the team: A list of names and images of the board

Also in the same frame we would like 3 tiles titled The Environment, Entrepreneurship, Civic Engagement with an option to scroll over for additional information.

Lastly the link to donate should be featured prominently and several times along with cues that lead people to find out more about the facts and the Sustainable Funding page.

We prefer limited scrolling and would like to see a clean yet modern approach to this funding platform.

Thank you and looking forward!
Updates

Project Deadline Extended
Reason: Thank you! Our executive board has rescheduled our meeting so we'll need a few more days to coordinate. Much appreciated.

Target Market(s)

Haitians, Friends of Haiti, and Media who are potential donors, innovators and decision makers

Industry/Entity Type

Foundation

Coding

Coded - Design and coding required

Number of Pages Required

5+ page

Requirements
Must have
• emotionally engaging and informative
• asset-focused language
• motion enabled pictures
• links to donate
Nice to have
• scoll-over and pop-ups
• music
Should not have
• charity language
• denigrating language
• images that depict poverty or need

```html
<!DOCTYPE html>
<html lang="en">
<head>
<meta charset="utf-8">
<title>Selvane Community Trust</title>
<link href="https://fonts.googleapis.com/css2?family=Montserrat:wght@400;500;600;700&family=Open+Sans:wght@400;600&display=swap" rel="stylesheet">
<style>
:root{
  --red:#c1232d;
  --red-btn:#c9353e;
  --blue:#1b4d94;
  --white:#ffffff;
  --ink:#1f1f1f;
  --muted:#a3a3a3;
  --soft:#f3f3f3;
  --line:#e4e4e4;
}
*{box-sizing:border-box;margin:0;padding:0}
html,body{width:1200px;height:3523px;overflow:hidden}
body{font-family:"Open Sans",Arial,sans-serif;color:var(--ink);background:var(--white);position:relative}
.abs{position:absolute}
.brand{display:flex;align-items:center;justify-content:center;gap:12px}
.brand-dot{width:34px;height:34px;border:2px solid var(--blue);border-radius:50%}
.brand-name{font-family:"Montserrat",Arial,sans-serif;font-weight:600;font-size:20px;color:var(--red);letter-spacing:1px;line-height:1}
.site-header{top:0;left:0;width:1200px;height:101px}
.site-header .brand{height:101px}
.main-nav{top:101px;left:0;width:1200px;height:71px;background:var(--red);display:flex;justify-content:center;align-items:center;gap:30px}
.main-nav a{font-family:"Montserrat",Arial,sans-serif;font-weight:700;font-size:12px;color:var(--white);text-decoration:none;text-transform:uppercase;padding:8px 0;letter-spacing:.2px}
.main-nav a.current{border-bottom:2px solid var(--white)}
.hero{top:172px;left:0;width:1200px;height:548px;background:linear-gradient(110deg,#6b5a2a 0%,#b08a5c 30%,#d9b58e 48%,#a7a046 70%,#5f7a1f 100%)}
.hero-title{top:420px;left:0;width:1200px;text-align:center;font-family:"Montserrat",Arial,sans-serif;font-weight:600;font-size:48px;color:var(--white)}
.hero-sub{top:493px;left:0;width:1200px;text-align:center;font-size:13px;color:var(--white)}
.btn{display:flex;align-items:center;justify-content:center;font-family:"Montserrat",Arial,sans-serif;font-weight:700;font-size:12px;color:var(--white);text-transform:uppercase;text-decoration:none}
.btn-blue{background:var(--blue);border-radius:4px}
.btn-red{background:var(--red-btn);border-radius:24px}
.hero .btn,.hero-btn{top:531px;left:507px;width:186px;height:47px}
.hero-dots{top:661px;left:0;width:1200px;display:flex;justify-content:center;gap:8px}
.hero-dots span{width:16px;height:16px;border:2px solid var(--white);border-radius:50%}
.intro{top:720px;left:0;width:1200px;height:328px;background:var(--soft)}
.section-title{position:absolute;left:0;width:1200px;text-align:center;font-family:"Montserrat",Arial,sans-serif;font-weight:600;font-size:33px}
.title-red{color:var(--red)}
.title-blue{color:var(--blue)}
.intro .section-title{top:70px}
.intro-text{top:140px;left:235px;width:730px;text-align:center;font-size:15px;line-height:1.75;color:var(--muted)}
.intro-btn{top:227px;left:507px;width:186px;height:47px}
.works .section-title{top:1104px}
.card{width:390px}
.card-photo{width:390px;height:226px}
.card-title{font-family:"Montserrat",Arial,sans-serif;font-size:16px;color:var(--red);margin-top:27px}
.card-text{font-size:12px;line-height:1.9;color:var(--muted);margin-top:12px;padding-right:20px}
.card-rule{height:1px;background:var(--line);margin-top:24px}
.card-foot{display:flex;justify-content:space-between;align-items:flex-start;margin-top:20px}
.fund-label{font-family:"Montserrat",Arial,sans-serif;font-size:11px;font-weight:500;color:var(--ink)}
.fund-amount{font-family:"Montserrat",Arial,sans-serif;font-size:34px;font-weight:500;color:var(--ink);line-height:1.2;margin-top:4px}
.card .btn{width:144px;height:36px;margin-top:4px}
.works-arrows{top:2188px;left:0;width:1200px;display:flex;justify-content:center;gap:26px}
.team{top:2275px;left:0;width:1200px;height:447px;background:var(--soft)}
.team .section-title{top:60px}
.member{top:131px;width:174px;text-align:center}
.member-photo{width:174px;height:165px;border:5px solid var(--white);box-shadow:0 2px 5px rgba(0,0,0,.18)}
.member-name{font-family:"Montserrat",Arial,sans-serif;font-weight:700;font-size:16px;color:var(--red);margin-top:20px}
.member-role{font-size:11px;color:#777;margin-top:8px}
.contact .section-title{top:2788px}
.field{left:270px;width:320px;height:47px;border:1px solid var(--line);border-radius:3px;padding:14px 16px;font-size:12px;color:#b3b3b3}
.field-msg{height:113px}
.send-btn{top:3264px;left:270px;width:146px;height:38px}
.contact-divider{top:2915px;left:625px;width:1px;height:400px;background:var(--line)}
.address{top:2940px;left:667px;font-size:12px;line-height:1.95;color:#555}
.address .label{font-family:"Montserrat",Arial,sans-serif;font-weight:700;color:var(--red);margin-bottom:32px}
.address .gap{height:28px}
.site-footer{top:3360px;left:0;width:1200px;height:163px;border-top:1px solid var(--line)}
.site-footer .brand{margin-top:28px}
.copyright{position:absolute;top:106px;left:0;width:1200px;text-align:center;font-size:12px;color:#333}
</style>
</head>
<body>

<header class="site-header abs">
  <div class="brand"><span class="brand-dot"></span><span class="brand-name">SELVANE COMMUNITY TRUST</span></div>
</header>

<nav class="main-nav abs">
  <a class="current" href="#">Home</a>
  <a href="#">About Us</a>
  <a href="#">Impact/Our Work/Projects</a>
  <a href="#">Donate</a>
  <a href="#">Contact Us</a>
  <a href="#">Meet the Team</a>
  <a href="#">Haiti's Assets</a>
</nav>

<section class="hero abs" role="img" aria-label="Photo of two hands holding each other against a soft green background"></section>
<h1 class="hero-title abs">Selvane Community Trust</h1>
<p class="hero-sub abs">Sed ut perspiciatis unde omnis iste natus error sit voluptatem accusantium...</p>
<a class="btn btn-blue hero-btn abs" href="#">Donate Now</a>
<div class="hero-dots abs"><span></span><span></span><span></span><span></span></div>

<section class="intro abs">
  <h2 class="section-title title-red">Selvane Community Trust</h2>
  <p class="intro-text abs">Selvane Community Trust is a grant-making agency that seeks to build an emotionally engaging and informative site that portrays Haiti from an asset lens.</p>
  <a class="btn btn-blue intro-btn abs" href="#">Contact Us</a>
</section>

<section class="works">
  <h2 class="section-title title-red">Our Works</h2>

  <article class="card abs" style="top:1189px;left:200px">
    <div class="card-photo" role="img" aria-label="Photo of many hands stacked together in a team gesture" style="background:linear-gradient(135deg,#4f7fb0,#c97a4a 55%,#e0642a)"></div>
    <h3 class="card-title">Community Trust</h3>
    <p class="card-text">Nemo enim ipsam voluptatem quia voluptas sit aspernatur aut odit aut fugit, sed quia consequuntur</p>
    <div class="card-rule"></div>
    <div class="card-foot"><div><div class="fund-label">Total Fund Invested</div><div class="fund-amount">$20,202</div></div><a class="btn btn-red" href="#">Donate Now</a></div>
  </article>

  <article class="card abs" style="top:1189px;left:609px">
    <div class="card-photo" role="img" aria-label="Photo of paper cut-out figures holding hands in a circle" style="background:linear-gradient(135deg,#dfe7ee,#a9b8c6 60%,#8796a6)"></div>
    <h3 class="card-title">Community Trust</h3>
    <p class="card-text">Nemo enim ipsam voluptatem quia voluptas sit aspernatur aut odit aut fugit, sed quia consequuntur</p>
    <div class="card-rule"></div>
    <div class="card-foot"><div><div class="fund-label">Total Fund Invested</div><div class="fund-amount">$20,202</div></div><a class="btn btn-red" href="#">Donate Now</a></div>
  </article>

  <article class="card abs" style="top:1680px;left:200px">
    <div class="card-photo" role="img" aria-label="Photo of a group of smiling children" style="background:linear-gradient(135deg,#7a5a44,#c79a7c 50%,#8e6a8a)"></div>
    <h3 class="card-title">Community Trust</h3>
    <p class="card-text">Nemo enim ipsam voluptatem quia voluptas sit aspernatur aut odit aut fugit, sed quia consequuntur</p>
    <div class="card-rule"></div>
    <div class="card-foot"><div><div class="fund-label">Total Fund Invested</div><div class="fund-amount">$20,202</div></div><a class="btn btn-red" href="#">Donate Now</a></div>
  </article>

  <article class="card abs" style="top:1680px;left:609px">
    <div class="card-photo" role="img" aria-label="Photo of people working together at a computer in a library" style="background:linear-gradient(135deg,#4a3a30,#8a6e5a 50%,#7a2e3a)"></div>
    <h3 class="card-title">Community Trust</h3>
    <p class="card-text">Nemo enim ipsam voluptatem quia voluptas sit aspernatur aut odit aut fugit, sed quia consequuntur</p>
    <div class="card-rule"></div>
    <div class="card-foot"><div><div class="fund-label">Total Fund Invested</div><div class="fund-amount">$20,202</div></div><a class="btn btn-red" href="#">Donate Now</a></div>
  </article>

  <div class="works-arrows abs">
    <svg width="16" height="26" viewBox="0 0 16 26" aria-label="Previous"><path d="M13 2 L3 13 L13 24" fill="none" stroke="#333" stroke-width="3"/></svg>
    <svg width="16" height="26" viewBox="0 0 16 26" aria-label="Next"><path d="M3 2 L13 13 L3 24" fill="none" stroke="#333" stroke-width="3"/></svg>
  </div>
</section>

<section class="team abs">
  <h2 class="section-title title-blue">Meet The Team</h2>
  <div class="member abs" style="left:207px">
    <div class="member-photo" role="img" aria-label="Portrait of board member Darel Vonne" style="background:linear-gradient(#9aa0a6,#4a5560)"></div>
    <div class="member-name">Darel Vonne</div><div class="member-role">CEO</div>
  </div>
  <div class="member abs" style="left:414px">
    <div class="member-photo" role="img" aria-label="Portrait of board member Tobin Hale" style="background:linear-gradient(#8a8d90,#3a3f46)"></div>
    <div class="member-name">Tobin Hale</div><div class="member-role">CEO</div>
  </div>
  <div class="member abs" style="left:616px">
    <div class="member-photo" role="img" aria-label="Portrait of board member Mira Calloway" style="background:linear-gradient(#f1dc8c,#c9964a)"></div>
    <div class="member-name">Mira Calloway</div><div class="member-role">CEO</div>
  </div>
  <div class="member abs" style="left:818px">
    <div class="member-photo" role="img" aria-label="Portrait of board member Ansel Brook" style="background:linear-gradient(#5a6470,#2a2f38)"></div>
    <div class="member-name">Ansel Brook</div><div class="member-role">CEO</div>
  </div>
</section>

<section class="contact">
  <h2 class="section-title title-blue">Contact Us</h2>
  <div class="field abs" style="top:2905px">Name</div>
  <div class="field abs" style="top:2977px">E-mail</div>
  <div class="field abs" style="top:3050px">Phone</div>
  <div class="field field-msg abs" style="top:3123px">Message</div>
  <a class="btn btn-red send-btn abs" href="#">Send</a>
  <div class="contact-divider abs"></div>
  <div class="address abs">
    <div class="label">Address</div>
    <div>Orin 42 Str. 10871, Velmara</div>
    <div>Tessaly, Corvane</div>
    <div class="gap"></div>
    <div>+30-2105550142 (landline)</div>
    <div>+30-2105550187 (fax)</div>
    <div class="gap"></div>
    <div>info@selvanecommunitytrust.org</div>
  </div>
</section>

<footer class="site-footer abs">
  <div class="brand"><span class="brand-dot"></span><span class="brand-name">SELVANE COMMUNITY TRUST</span></div>
  <p class="copyright">© 2016 Company Name | All Rights Reserved</p>
</footer>

</body>
</html>
```